Harlow Street Players Poster, Flyer, & Corflute Design

Technical requirements: We need designs for an A3 sized poster, a trifold double side A4 sized flyer, and a standard corflute, to advertise our open day, on the .27th of February, 2016 at 12 Dunmore Rd, Watson, ACT. Dates must be in the Australian format: dd/mm/yy or dd/mm/yyyy.
The date sections on all of the designs must be editable, and the flyer must have large sections of content which are easily editable. The flyer must have the room to talk about the history of the organisation, its current size and structure, current programmes, how to join, etc.
All can be full colour.
Artistic requirements: The designs must incorporate our logo (attached), the organisational colours (gold, white, and navy blue), and must achieve three goals. They must:
- Portray the organisation as a fun, diverse, and exciting community of musicians;
- Encourage people to come and participate in our open day and eventually join the organisation.
- Reflect the diverse styles of music the organisation plays, and make jazz and classical music attractive.
Design guidelines:
Ideally the designs should be simple, uncluttered and beautiful. They should focus on conveying information.. They should showcase the band's colours and draw on classic images and designs from jazz and concert band history. They should be eye catching.
Organisational background:
Harlow Street Players was established in 1925 and has a long standing history as the band of Canberra.
HSP supports a variety of ensembles including:
1. Fledgling Wind Group for beginner students.
2. Rising Reed Group for young musicians eager to push their skills to a higher level.
3. Peter Lomond Group, a recreational concert band for those new to an instrument or returning after an absence.
4. Halcyon Swing Crew - a semi-professional big band.
5. Harlow Street Players - A-grade wind ensemble recently runner up at the Federal Brass Trophy Series in Sydney
6. The Ardley Reeds & Horns - flexible, professional chamber wind and brass ensembles.
Regardless of your level, we want to hear from you as Harlow Street Players is always keen to take on new players. We play for a variety of community events throughout the year and if you don't want to play, come have a listen!

```html
<!DOCTYPE html>
<html lang="en">
<head>
<meta charset="utf-8">
<title>Harlow Street Players – Alternative Jazz Concert</title>
<link rel="stylesheet" href="https://fonts.googleapis.com/css2?family=Oswald:wght@300;400;500;700&family=Comfortaa:wght@700&family=Josefin+Sans:wght@300;700&family=Arimo:wght@700&display=swap">
<style>
  :root {
    --navy: #1c54a3;
    --navy-deep: #123c7c;
    --yellow: #f3e522;
    --gold-light: #e9b63c;
    --gold-dark: #b98318;
    --white: #ffffff;
    --pale: #f3ea9a;
    --footer: #ffffff;
    --ink: #1c3a6e;
  }
  html, body { margin: 0; padding: 0; overflow: hidden; background: #e8e8e8; }
  .poster {
    position: relative; width: 847px; height: 1200px; overflow: hidden;
    background: var(--navy); font-family: "Oswald", sans-serif; color: var(--white);
  }
  .gold-band {
    position: absolute; left: 576px; top: 0; width: 271px; height: 615px;
    background: linear-gradient(90deg, var(--gold-light), var(--gold-dark));
  }
  .band-title {
    position: absolute; left: 585px; top: 8px; margin: 0;
    font: 700 36px/1.0 "Oswald", sans-serif; color: var(--white); text-transform: uppercase;
  }
  .guitar-art {
    position: absolute; left: 540px; top: 180px; width: 290px; height: 510px;
    border-radius: 140px 140px 60px 60px;
    background: linear-gradient(160deg, #2f6bc4, var(--navy-deep));
  }
  .festival-name {
    position: absolute; left: 40px; top: 20px; margin: 0;
    font: 400 36px/1 "Oswald", sans-serif; letter-spacing: 1px;
  }
  .alt-line {
    position: absolute; left: 40px; top: 84px; margin: 0;
    font: 300 50px/1 "Josefin Sans", sans-serif; letter-spacing: 6px;
  }
  .jazz {
    position: absolute; left: 28px; top: 130px; margin: 0;
    font: 700 168px/1 "Comfortaa", sans-serif; color: var(--yellow); letter-spacing: -6px;
  }
  .concert {
    position: absolute; left: 40px; top: 345px; margin: 0;
    font: 300 50px/1 "Josefin Sans", sans-serif; letter-spacing: 10px;
  }
  .tagline {
    position: absolute; left: 90px; top: 404px; margin: 0;
    font: 700 20px/1 "Arimo", sans-serif; color: var(--yellow);
  }
  .venue {
    position: absolute; left: 40px; top: 444px; margin: 0;
    font: 500 52px/1.12 "Oswald", sans-serif; letter-spacing: 2px; text-transform: uppercase;
  }
  .date {
    position: absolute; left: 40px; top: 568px; margin: 0;
    font: 300 66px/1 "Oswald", sans-serif; letter-spacing: 2px;
  }
  .doors {
    position: absolute; left: 266px; top: 580px; margin: 0; padding-left: 10px;
    border-left: 3px solid var(--yellow);
    font: 700 18px/1.2 "Arimo", sans-serif; color: var(--yellow);
  }
  .tickets {
    position: absolute; left: 40px; top: 664px; margin: 0;
    font: 400 17px/1 "Arimo", sans-serif; font-weight: 700; color: var(--white);
  }
  .invite {
    position: absolute; left: 40px; top: 712px; width: 770px; margin: 0;
    font: 400 19px/1.18 "Oswald", sans-serif; letter-spacing: 1.5px; text-transform: uppercase;
  }
  .listen {
    position: absolute; left: 40px; top: 832px; margin: 0;
    font: 700 35px/1 "Oswald", sans-serif; color: var(--yellow); text-transform: uppercase;
  }
  .background-note {
    position: absolute; left: 0; top: 980px; width: 847px; margin: 0; text-align: center;
    font: 700 19px/1.3 "Arimo", sans-serif; color: var(--pale);
  }
  .footer {
    position: absolute; left: 0; top: 1096px; width: 847px; height: 104px; background: var(--footer);
  }
  .client-mark { position: absolute; left: 24px; top: 22px; display: flex; align-items: center; gap: 14px; }
  .client-mark .dot { width: 60px; height: 60px; border-radius: 50%; background: var(--navy); }
  .client-mark .name { font: 500 30px/1 "Oswald", sans-serif; color: var(--ink); }
  .supporters { position: absolute; right: 20px; top: 14px; width: 270px; }
  .supporters .label { margin: 0 0 4px 0; font: 400 12px/1 "Arimo", sans-serif; color: var(--ink); text-align: right; }
  .badges { display: flex; justify-content: flex-end; gap: 14px; }
  .badge { background: var(--navy); }
  .badge.round { width: 64px; height: 64px; border-radius: 50%; }
  .badge.square { width: 64px; height: 64px; }
  .badge.small { width: 44px; height: 44px; margin-top: 10px; }
</style>
</head>
<body>
<main class="poster">
  <div class="gold-band"></div>
  <h2 class="band-title">Classical<br>and jazz<br>music<br>festival</h2>
  <div class="guitar-art" role="img" aria-label="Illustration of a blue electric guitar"></div>

  <p class="festival-name">CANABERA MUSIC FESTIVAL:</p>
  <p class="alt-line">ALTERNATIVE</p>
  <h1 class="jazz">JAZZ</h1>
  <p class="concert">CONCERT</p>
  <p class="tagline">A one-day festival of pure classical sounds</p>
  <p class="venue">12 Dunmore Rd,<br>Watson, ACT.</p>
  <p class="date"><time datetime="2016-02-27">27.02.16</time></p>
  <p class="doors">doors open<br>from 3<br>to 11 pm</p>
  <p class="tickets">tickets almost solt out! buy yours and save the date</p>
  <p class="invite">Regardless of your level, we want to hear from you as Harlow Street Players is always keen to take on new players. We play for a variety of c ommunity events throughout the year and if</p>
  <p class="listen">You don't want to play, come have a listen!</p>

  <p class="background-note">Organisational background:<br>Harlow Street Players was established in 1925<br>and has a long standing history as the band of</p>

  <footer class="footer">
    <div class="client-mark">
      <span class="dot"></span>
      <span class="name">Harlow Street Players</span>
    </div>
    <div class="supporters">
      <p class="label">Supported by</p>
      <div class="badges">
        <span class="badge round"></span>
        <span class="badge square"></span>
        <span class="badge small"></span>
      </div>
    </div>
  </footer>
</main>
</body>
</html>
```